Modern, cutting edge crypto trading website.

I need a single-page website design, approximate 4-5 pages. I have included a screenshot of the inside of the current application for some reference for what it currently looks like. This is the public side of the application for not logged in users.

I am currently thinking about 3-5 sections of the page.
Menu at top is optional, these could be the sections of the site.
1. Above the fold cool, grabbing stuff.
2. What problem does this solve
3. Additional benefits
4. Pricing
5. Open to ideas! Well it's all open to ideas if you have ideas.

I am nervous about hiring designers, I am open to a further discussion for more work for additional money but I have to LIKE your design. So this could be considered a trial. I would like to continue to design the application itself and match everything together!

I really like the tradewisp website.

Competitor websites:
https://7ridges.example/
https://www.tradewisp.example/

Target Market(s)

Adults 25-50 mostly male,

Number of Pages Required

4 page

Colors

Designer to choose colors to be used in the design.

Requirements
Must have
• Modern design, clean lines, professional.
Nice to have
• Fun SVG stuff. Not for this price, but in the future.
Should not have
• Should not be cluttered OR too spacey. Quince's website has too much open space sometimes.

```html
<!DOCTYPE html>
<html lang="en">
<head>
<meta charset="utf-8">
<title>Corvane — Crypto Trading</title>
<link href="https://fonts.googleapis.com/css2?family=Poppins:wght@400;500;600;700;800&display=swap" rel="stylesheet">
<style>
:root{
  --navy:#2238a0;
  --navy-deep:#1f3596;
  --cyan:#4ad8f5;
  --ink:#1c1d2b;
  --muted:#4a4b5c;
  --line:#e7e8f0;
  --white:#ffffff;
}
*{margin:0;padding:0;box-sizing:border-box}
html,body{width:1200px;height:3726px;overflow:hidden;background:var(--white)}
body{position:relative;font-family:'Poppins',sans-serif;color:var(--ink)}
.abs{position:absolute}
.bg-shapes{position:absolute;left:0;top:0;width:1200px;height:3726px}

/* nav */
.brand{left:160px;top:54px;display:flex;align-items:center;gap:10px;color:var(--white);font-weight:700;font-size:20px;line-height:52px;top:54px}
.brand-dot{width:52px;height:52px;border-radius:50%;background:var(--white)}
.nav{left:272px;top:47px;display:flex;gap:0;font-size:12px;font-weight:500;color:var(--white);letter-spacing:.2px}
.nav a{color:inherit;text-decoration:none;position:absolute;white-space:nowrap}
.nav a.active{color:var(--cyan);border-bottom:1px solid var(--cyan);padding-bottom:2px}
.btn{display:flex;align-items:center;justify-content:center;font-weight:700;font-size:12px;text-transform:uppercase;letter-spacing:.2px;border-radius:3px;text-decoration:none}
.btn-login{left:814px;top:38px;width:106px;height:36px;background:var(--white);color:var(--cyan)}
.btn-signup{left:935px;top:38px;width:105px;height:36px;background:var(--cyan);color:var(--white)}

/* hero */
.hero-title{left:160px;top:160px;width:460px;font-weight:800;font-size:40px;line-height:59px;color:var(--white);letter-spacing:-.3px}
.hero-text{left:160px;top:343px;width:440px;font-size:11px;line-height:23px;color:#e6e9ff;letter-spacing:.4px}
.btn-discover{left:160px;top:415px;width:160px;height:53px;background:var(--cyan);color:var(--white)}
.art{border-radius:24px}

/* shared section type */
.eyebrow{font-size:14px;font-weight:600;color:var(--navy);letter-spacing:1px}
.eyebrow-rule{height:2px;background:var(--navy)}
.h2{font-weight:600;font-size:24px;line-height:30px;letter-spacing:2px;color:var(--ink)}
.body{font-size:13px;line-height:22.5px;color:var(--muted);letter-spacing:.6px}
.btn-navy{background:var(--navy-deep);color:var(--white)}

.play{left:535px;top:998px;width:38px;height:38px;border-radius:50%;background:var(--navy)}
.watch{left:584px;top:1001px;font-size:11px;font-weight:600;color:var(--navy);letter-spacing:.5px}
.watch small{display:block;font-size:7px;font-weight:400;color:var(--cyan);text-decoration:underline;letter-spacing:.3px;margin-top:1px}

.center{left:0;width:1200px;text-align:center}

/* steps */
.card{position:absolute;border:2px solid var(--navy);border-radius:4px;background:var(--white);text-align:center}
.card.featured{background:var(--navy-deep);border-color:var(--navy-deep)}
.card h3{font-size:15px;font-weight:600;color:var(--ink);letter-spacing:.6px;position:absolute;left:0;right:0}
.card.featured h3{color:var(--white)}
.card p{position:absolute;left:24px;right:24px;font-size:11px;line-height:22.5px;color:var(--muted);letter-spacing:.4px}
.card.featured p{color:#e6e9ff}
.card .rule{position:absolute;left:50%;width:75px;margin-left:-37px;height:2px;background:var(--cyan)}
.badge{position:absolute;width:88px;height:88px;border-radius:50%;border:2px solid var(--navy);background:var(--white);display:flex;align-items:center;justify-content:center}
.badge.filled{background:var(--cyan);border:4px solid var(--white);width:92px;height:92px}

/* benefits */
.lead{left:158px;top:2731px;width:520px;font-size:16.5px;line-height:23px;color:var(--ink);letter-spacing:.3px}
.ticks{left:158px;top:2830px;list-style:none}
.ticks li{display:flex;align-items:center;gap:12px;height:37.7px;font-size:13px;color:var(--muted);letter-spacing:.6px}
.tick{width:21px;height:21px;border-radius:50%;background:var(--navy);display:flex;align-items:center;justify-content:center;flex:none}

/* contact */
.contact-title{top:3478px;font-size:32px;font-weight:700;color:var(--white);letter-spacing:1px}
.contact-sub{top:3537px;font-size:14px;color:#e6e9ff;letter-spacing:.5px}
.chan{position:absolute;top:3604px;width:120px;text-align:center;font-size:8.5px;color:#e6e9ff}
.chan .ring{width:44px;height:44px;border-radius:50%;background:var(--white);margin:0 auto 8px;display:flex;align-items:center;justify-content:center}
</style>
</head>
<body>

<svg class="bg-shapes" viewBox="0 0 1200 3726" aria-hidden="true">
  <!-- hero band -->
  <path d="M0 0H1200V665C1000 650 700 620 420 595C250 580 120 560 60 500C30 470 10 430 0 400Z" fill="#2238a0"/>
  <path d="M0 410C20 440 45 480 48 515C50 545 30 562 0 562Z" fill="#2238a0"/>
  <path d="M935 660L1200 420V665Z" fill="#2a42ad" opacity=".5"/>
  <!-- side blob -->
  <path d="M1200 894C1172 894 1158 910 1158 935C1158 950 1170 972 1200 1012Z" fill="#2238a0"/>
  <!-- step arrows -->
  <g fill="none" stroke="#d6d8e4" stroke-width="2.5" stroke-linecap="round" stroke-linejoin="round">
    <path d="M396 1848C402 1832 416 1824 432 1826"/><path d="M424 1818L434 1826L424 1834"/>
    <path d="M764 1818C782 1826 790 1840 784 1854"/><path d="M776 1848L784 1856L792 1846"/>
    <path d="M804 2218C796 2236 782 2244 766 2242"/><path d="M774 2234L764 2242L774 2250"/>
  </g>
  <!-- footer band -->
  <path d="M0 3203L138 3238Q152 3243 152 3262L152 3270L1200 3450V3726H0Z" fill="#2238a0"/>
  <path d="M1200 3410C1230 3470 1200 3560 1200 3560Z" fill="#2238a0"/>
  <path d="M905 3726C930 3660 1020 3610 1110 3610C1150 3610 1180 3620 1200 3630" fill="none" stroke="#8ea0e8" stroke-width="1.5" stroke-dasharray="6 6"/>
  <path d="M968 3726C990 3690 1040 3675 1090 3675C1150 3675 1200 3700 1200 3700V3726Z" fill="#4ad8f5"/>
</svg>

<!-- header -->
<div class="abs brand"><span class="brand-dot"></span>Corvane</div>
<nav class="abs nav" aria-label="Primary">
  <a class="active" href="#" style="left:0">HOME</a>
  <a href="#" style="left:63px">ABOUT</a>
  <a href="#" style="left:131px">SERVICES</a>
  <a href="#" style="left:214px">BENEFITS</a>
  <a href="#" style="left:293px">HOW IT WORKS</a>
  <a href="#" style="left:409px">CONTACT US</a>
</nav>
<a class="abs btn btn-login" href="#">Login</a>
<a class="abs btn btn-signup" href="#">Sign up</a>

<!-- hero -->
<h1 class="abs hero-title">Lorem Ipsum Dolores Poistedam Currency Best Award</h1>
<p class="abs hero-text">Lorem ipsum dolor sit amet, consetetur sadipscing elitr, sed diam if a nonumy eirmod tempor invidunt ut</p>
<a class="abs btn btn-discover" href="#">Discover more</a>
<div class="abs art" role="img" aria-label="Isometric stack of coins floating above a glowing platform with hexagon grid" style="left:640px;top:125px;width:395px;height:420px;background:radial-gradient(circle at 55% 55%,#7b5de0 0%,#4a4fc8 40%,rgba(34,56,160,0) 72%)"></div>

<!-- about -->
<div class="abs art" role="img" aria-label="Isometric trader standing at a large data screen on a round platform with charts" style="left:137px;top:723px;width:333px;height:362px;background:radial-gradient(ellipse at 50% 65%,#4b3aa8 0%,#7b82d8 45%,#d8f6ff 70%,rgba(255,255,255,0) 80%)"></div>
<div class="abs eyebrow" style="left:536px;top:765px">About</div>
<div class="abs eyebrow-rule" style="left:536px;top:794px;width:113px"></div>
<h2 class="abs h2" style="left:536px;top:820px;width:420px">Lorem Ipsum Dolor Amet Ningun Postekam Iftim</h2>
<p class="abs body" style="left:536px;top:903px;width:510px">Sed diam voluptua. At vero eos et accusam et justo duo dolores et ea rebum. Stet clita kasd gubergren, no sea takimata sanctus est Lorem a ipsum dolor sit amet</p>
<div class="abs play"><svg width="38" height="38" viewBox="0 0 38 38"><path d="M15 12L26 19L15 26Z" fill="#fff"/></svg></div>
<div class="abs watch">Watch Intro Video<small>How it works</small></div>

<!-- problem -->
<div class="abs eyebrow" style="left:163px;top:1210px">Lorem Ipsum</div>
<div class="abs eyebrow-rule" style="left:163px;top:1240px;width:108px"></div>
<h2 class="abs h2" style="left:163px;top:1265px;width:420px">Lorem ipsum dolor amet locavore stumptown four</h2>
<p class="abs body" style="left:163px;top:1349px;width:420px">Lorem ipsum dolor amet ningun postekam valar dohaeris postedam if any crypto</p>
<a class="abs btn btn-navy" href="#" style="left:160px;top:1421px;width:160px;height:54px">Try it now</a>
<div class="abs art" role="img" aria-label="Isometric city block of purple towers around a laptop on a glowing base" style="left:622px;top:1142px;width:383px;height:391px;background:radial-gradient(ellipse at 50% 60%,#9a6ef0 0%,#c9b6f5 40%,#dff7ff 62%,rgba(255,255,255,0) 76%)"></div>

<!-- network decorations -->
<div class="abs" role="img" aria-label="Faint network of connected dots" style="left:955px;top:1370px;width:245px;height:500px;background:linear-gradient(160deg,rgba(200,202,214,0) 0%,rgba(200,202,214,.18) 50%,rgba(200,202,214,0) 100%)"></div>
<div class="abs" role="img" aria-label="Faint network of connected dots" style="left:0;top:2205px;width:275px;height:530px;background:linear-gradient(200deg,rgba(200,202,214,0) 0%,rgba(200,202,214,.18) 50%,rgba(200,202,214,0) 100%)"></div>

<!-- how it works -->
<div class="abs eyebrow center" style="top:1601px">What To Do</div>
<div class="abs eyebrow-rule" style="left:555px;top:1630px;width:100px"></div>
<h2 class="abs h2 center" style="top:1656px">How To Get Started Here</h2>

<div class="card" style="left:162px;top:1909px;width:276px;height:260px">
  <h3 style="top:66px">Create Your Wallet</h3>
  <p style="top:136px">Lorem ipsum dolor amet locavore stumptown four loko, vaporware tote bag neutra hexagon</p>
</div>
<div class="badge" style="left:255px;top:1862px"><svg width="44" height="44" viewBox="0 0 44 44" fill="none" stroke="#2238a0" stroke-width="1.6"><rect x="6" y="14" width="32" height="22" rx="3"/><path d="M28 22h10v8H28z"/><circle cx="32" cy="26" r="1.4"/><rect x="16" y="6" width="12" height="10" rx="2"/></svg></div>

<div class="card featured" style="left:463px;top:1803px;width:277px;height:262px">
  <h3 style="top:70px">Start Trading Coins</h3>
  <div class="rule" style="top:116px"></div>
  <p style="top:140px">Lorem ipsum dolor amet locavore stumptown four loko, vaporware tote bag neutra hexagon</p>
</div>
<div class="badge filled" style="left:555px;top:1756px"><svg width="54" height="40" viewBox="0 0 54 40" fill="none" stroke="#fff" stroke-width="1.8"><rect x="4" y="12" width="24" height="14" rx="2"/><circle cx="16" cy="19" r="4"/><circle cx="40" cy="19" r="9"/><path d="M14 4a20 20 0 0 1 24 2M40 36a20 20 0 0 1-24-2"/></svg></div>

<div class="card" style="left:761px;top:1909px;width:277px;height:260px">
  <h3 style="top:66px">Raise Your Profit</h3>
  <p style="top:136px">Lorem ipsum dolor amet locavore stumptown four loko, vaporware tote bag neutra hexagon</p>
</div>
<div class="badge" style="left:855px;top:1862px"><svg width="44" height="44" viewBox="0 0 44 44" fill="none" stroke="#2238a0" stroke-width="1.6"><circle cx="14" cy="12" r="7"/><rect x="8" y="30" width="5" height="8"/><rect x="17" y="26" width="5" height="12"/><rect x="26" y="22" width="5" height="16"/><rect x="35" y="16" width="5" height="22"/><path d="M22 18l14-10M32 8h4v4"/></svg></div>

<div class="card" style="left:458px;top:2134px;width:277px;height:261px">
  <h3 style="top:66px">Extend Earnings</h3>
  <div class="rule" style="top:114px"></div>
  <p style="top:139px">Lorem ipsum dolor amet locavore stumptown four loko, vaporware tote bag neutra hexagon</p>
</div>
<div class="badge" style="left:552px;top:2087px"><svg width="44" height="44" viewBox="0 0 44 44" fill="none" stroke="#2238a0" stroke-width="1.6"><rect x="15" y="15" width="14" height="14" rx="2"/><path d="M6 10h32M6 34h32M10 6v32M34 6v32" stroke="#4ad8f5" stroke-dasharray="2 3"/></svg></div>

<!-- benefits -->
<div class="abs eyebrow center" style="top:2522px">Why Using It?</div>
<div class="abs eyebrow-rule" style="left:548px;top:2550px;width:108px"></div>
<h2 class="abs h2 center" style="top:2575px">Some Of The Benefits Here</h2>
<p class="abs lead">Lorem ipsum dolor amet locavore stumptown four loko, vde a aporware tote bag neutra hexagon. Dreamcatcher health goth affogato letterpress, hoodie migas taiyaki VHS sartorial</p>
<ul class="abs ticks">
  <li><span class="tick"><svg width="11" height="9" viewBox="0 0 11 9"><path d="M1 4.5L4 7.5L10 1" fill="none" stroke="#fff" stroke-width="1.8"/></svg></span>Lorem Pisum Dolor Amet Ningun Postekam Valar Dohaeris Aet</li>
  <li><span class="tick"><svg width="11" height="9" viewBox="0 0 11 9"><path d="M1 4.5L4 7.5L10 1" fill="none" stroke="#fff" stroke-width="1.8"/></svg></span>Lorem Pisum Dolor Amet Ningun Postekam Valar Dohaeris</li>
  <li><span class="tick"><svg width="11" height="9" viewBox="0 0 11 9"><path d="M1 4.5L4 7.5L10 1" fill="none" stroke="#fff" stroke-width="1.8"/></svg></span>Lorem Pisum Dolor Amet Ningun Postekam</li>
  <li><span class="tick"><svg width="11" height="9" viewBox="0 0 11 9"><path d="M1 4.5L4 7.5L10 1" fill="none" stroke="#fff" stroke-width="1.8"/></svg></span>Lorem Pisum Dolor Amet Ningun</li>
</ul>
<a class="abs btn btn-navy" href="#" style="left:160px;top:3012px;width:160px;height:53px">Create account</a>
<div class="abs art" role="img" aria-label="Laptop showing the trading dashboard with price charts" style="left:680px;top:2581px;width:433px;height:564px;background:radial-gradient(ellipse at 55% 50%,#c9ccd6 0%,#e4e6ec 45%,rgba(255,255,255,0) 72%)"></div>

<!-- contact -->
<h2 class="abs center contact-title">Contact Our Team</h2>
<p class="abs center contact-sub">Have any question? Please don't hesitate to reach out to us. We'll get back to you shortly</p>
<div class="chan" style="left:440px"><div class="ring"></div>@fanpage</div>
<div class="chan" style="left:536px"><div class="ring"><svg width="22" height="16" viewBox="0 0 22 16"><rect x="1" y="1" width="20" height="14" rx="2" fill="#4ad8f5"/><path d="M1 2l10 7 10-7" fill="none" stroke="#fff" stroke-width="1.6"/></svg></div>email@example.com</div>
<div class="chan" style="left:634px"><div class="ring"><svg width="20" height="20" viewBox="0 0 20 20"><path d="M4 2l4 0 1 5-2.5 1.5a11 11 0 0 0 5 5L13 11l5 1v4c0 1-1 2-2 2A16 16 0 0 1 2 4c0-1 1-2 2-2z" fill="#4ad8f5"/></svg></div>+123 456 789</div>

</body>
</html>
```